Create a bold and border around my logo to make it pop and sign graphic design

I would like someone to create a sign graphic design so I can use on the side of my trucks and put on yard signs. I would to remove a lot of the white and add more of the orange and blue to give it more pop when cars drive past. I would like the services to be removed and for you to leave space for a mobile number that i would add later. I don’t want my logo changed at all. I just want colour and design to be added to the background so i can use it in signage. Same colour as on the sign

```html
<!DOCTYPE html>
<html lang="en">
<head>
<meta charset="utf-8">
<title>Branchworthy – Vehicle & Yard Sign</title>
<link rel="stylesheet" href="https://fonts.googleapis.com/css2?family=Lexend:wght@600&family=Roboto:wght@400&display=swap">
<style>
  :root {
    --page-bg: #dcdcdc;
    --brand-blue: #034ea2;
    --brand-blue-light: #2f86e0;
    --brand-orange: #f17022;
    --brand-orange-light: #ffa640;
    --wordmark-blue: #3e56a8;
    --band-white: #ffffff;
    --text-dark: #111111;
  }
  * { box-sizing: border-box; margin: 0; padding: 0; }
  html, body {
    width: 1200px;
    height: 1000px;
    overflow: hidden;
    background: var(--page-bg);
  }
  .sign {
    position: absolute;
    left: 157px;
    top: 279px;
    width: 886px;
    height: 441px;
    overflow: hidden;
    background: var(--brand-orange);
  }
  .sign__band--blue {
    position: absolute;
    left: 0; top: 0;
    width: 100%; height: 148px;
    background: var(--brand-blue);
  }
  .sign__band--white {
    position: absolute;
    left: 0; top: 148px;
    width: 100%; height: 98px;
    background: var(--band-white);
  }
  .sign__glow {
    position: absolute;
    border-radius: 50%;
  }
  .sign__glow--blue {
    left: 560px; top: 0;
    width: 300px; height: 148px;
    background: radial-gradient(ellipse at 50% 80%, rgba(47,134,224,0.55), rgba(47,134,224,0) 70%);
    border-radius: 0;
  }
  .sign__glow--orange-left {
    left: 0; top: 246px;
    width: 300px; height: 195px;
    background: radial-gradient(ellipse at 40% 35%, rgba(255,166,64,0.55), rgba(255,166,64,0) 70%);
    border-radius: 0;
  }
  .sign__glow--orange-right {
    left: 620px; top: 246px;
    width: 260px; height: 120px;
    background: radial-gradient(ellipse at 50% 30%, rgba(255,166,64,0.45), rgba(255,166,64,0) 70%);
    border-radius: 0;
  }
  .sign__badge {
    position: absolute;
    left: 44px; top: 81px;
    width: 224px; height: 224px;
    border-radius: 50%;
    background: var(--band-white);
  }
  .sign__name {
    position: absolute;
    left: 273px; top: 160px;
    font-family: "Lexend", sans-serif;
    font-weight: 600;
    font-size: 60px;
    line-height: 70px;
    letter-spacing: 1px;
    color: var(--wordmark-blue);
    white-space: nowrap;
  }
  .sign__contact {
    position: absolute;
    left: 362px; top: 242px;
    width: 389px; height: 50px;
    border-radius: 25px;
    background: var(--band-white);
    display: flex;
    align-items: center;
    justify-content: center;
    font-family: "Roboto", sans-serif;
    font-weight: 400;
    font-size: 27px;
    color: var(--text-dark);
  }
</style>
</head>
<body>
  <main class="sign">
    <div class="sign__band--blue"></div>
    <div class="sign__glow sign__glow--blue" role="img" aria-label="Light blue halftone dot texture"></div>
    <div class="sign__band--white"></div>
    <div class="sign__glow sign__glow--orange-left" role="img" aria-label="Light orange halftone dot texture"></div>
    <div class="sign__glow sign__glow--orange-right" role="img" aria-label="Light orange halftone dot texture"></div>
    <div class="sign__badge"></div>
    <h1 class="sign__name">BRANCHWORTHY</h1>
    <p class="sign__contact">You can contact us here</p>
  </main>
</body>
</html>
```